Quarrybend Building Company / Website*

We need a design for a contracting company website based in KSA, something modern with the same color theme as the attached logo. including a page for people who want to submit their CV and try to apply for a job.Also to include the "about us, contact us, gallery, Divisions, Supplies, etc...". If possible to have an interactive or moving background. Please disregard the "Smart Solutions" Section in the attached profile.

Industry/Entity Type

Construction Company

Number of Pages Required

5+ page

Colors

Designer to choose colors to be used in the design.

Requirements
Must have
• Pages:
• about us, contact us, gallery, Divisions, Apply for a job, Supplies
Nice to have
• - Moving or interactive background

```html
<!DOCTYPE html>
<html lang="en">
<head>
<meta charset="utf-8">
<title>Quarrybend Building Company</title>
<link href="https://fonts.googleapis.com/css2?family=Montserrat:ital,wght@0,300;0,400;0,500;0,600;0,700;1,300;1,400&display=swap" rel="stylesheet">
<style>
:root{
  --orange:#f6ac25;
  --orange-dark:#e39a12;
  --ink:#1d1d1d;
  --text:#6e6e6e;
  --light:#f4f4f4;
  --line:#e6e6e6;
  --white:#ffffff;
  --dark:#222;
}
*{box-sizing:border-box;margin:0;padding:0}
html,body{width:1200px;height:3891px;overflow:hidden}
body{position:relative;font-family:"Montserrat",sans-serif;color:var(--ink);background:var(--white)}
.abs{position:absolute}
a{color:inherit;text-decoration:none}

/* top bar */
.topbar{left:0;top:0;width:1200px;height:38px;background:var(--orange);color:#fff;font-size:12px}
.topbar .phone{left:172px;top:12px}
.social{display:flex;gap:10px}
.topbar .social{right:176px;top:7px}
.social span{width:24px;height:24px;border-radius:50%;background:#222;display:block}
.topbar .social span{background:#fff}

/* header */
.header{left:0;top:38px;width:1200px;height:136px;background:#fff;box-shadow:0 2px 6px rgba(0,0,0,.08)}
.logo{left:150px;top:32px;width:130px;text-align:center;font-size:12px;font-weight:500;color:var(--ink)}
.logo .mark{width:16px;height:16px;background:var(--orange);margin:0 auto 6px}
.btn{display:inline-flex;align-items:center;justify-content:center;font-weight:600;font-size:10px;letter-spacing:.3px;color:#fff;text-transform:uppercase;border-radius:5px}
.btn-grad{background:linear-gradient(90deg,var(--orange) 0%,var(--orange-dark) 60%,#3a2a10 100%)}
.apply{left:903px;top:32px;width:125px;height:36px}
.nav{left:449px;top:86px;display:flex;gap:37px;font-size:13px;font-weight:500}
.search{left:1013px;top:86px}

/* hero */
.hero{left:0;top:174px;width:1200px;height:567px;background:linear-gradient(180deg,#8a8170 0%,#5a4b3a 55%,#2d241c 100%)}
.hero-text{left:0;top:345px;width:1200px;text-align:center;color:#fff}
.hero-text .w{font-size:22px;font-weight:500}
.hero-text .h{font-size:35px;font-weight:700;line-height:47px;margin-top:8px}
.hero-text .h em{font-style:normal;color:var(--orange)}
.hero .b1{left:465px;top:309px;width:124px;height:35px}
.hero .b2{left:612px;top:309px;width:124px;height:35px;border:2px solid #fff;background:transparent}
.arrow-box{width:33px;height:34px;background:#fff;border-radius:3px;display:flex;align-items:center;justify-content:center}

/* about */
.about-photo{left:184px;top:790px;width:302px;height:302px;border-radius:50%;background:linear-gradient(160deg,#cfd5d8,#8d959a 60%,#3f4448);border-left:6px solid var(--orange);border-top:6px solid var(--orange)}
h2{font-weight:700;font-size:27px;color:var(--ink)}
.rule{width:30px;height:2px;background:var(--orange)}
.about-title{left:543px;top:830px}
.about-text{left:540px;top:896px;width:490px;font-size:11.5px;line-height:19.5px;color:var(--text);font-weight:300}
.years{left:688px;top:1009px;width:84px;height:90px;border:2px solid var(--orange);display:flex;align-items:center;justify-content:center;font-size:50px;font-weight:600}
.years-label{left:786px;top:1037px;font-size:13.5px;font-weight:600;line-height:17px}

/* divisions */
.division{width:364px;height:160px;background:#fff;box-shadow:0 1px 10px rgba(0,0,0,.08);text-align:center;padding-top:50px}
.division h3{font-size:18px;font-weight:600}
.division p{font-size:11.5px;line-height:19px;color:var(--text);font-weight:300;width:290px;margin:12px auto 0}
.div-icon{width:60px;height:60px;border-radius:50%;background:#4a2a1c}

/* services */
.services-bg{left:0;top:1480px;width:1200px;height:480px;background:linear-gradient(180deg,#fff 0%,#f0f0f0 60%,#d6d6d6 100%)}
.center-title{left:0;width:1200px;text-align:center}
.center-rule{left:585px}
.service{width:272px;height:355px;background:#fff;border-radius:8px;overflow:hidden;box-shadow:0 2px 10px rgba(0,0,0,.1);text-align:center}
.service .band{height:132px;background:var(--orange)}
.service .ph{position:absolute;left:40px;top:68px;width:192px;height:150px;border:5px solid #fff;border-radius:4px}
.service h3{position:absolute;left:0;width:100%;top:236px;font-size:18px;font-weight:600;color:var(--orange)}
.service p{position:absolute;left:36px;width:200px;top:268px;font-size:11px;line-height:16px;color:#555}
.service .go{position:absolute;left:126px;top:338px}
.sm-arrow{width:24px;height:24px;background:var(--orange);border-radius:3px;display:flex;align-items:center;justify-content:center}

/* stats */
.stats{left:0;top:1960px;width:1200px;height:190px;background:linear-gradient(90deg,#f6b532,#f29f1a 50%,#f6b532);border-top:5px solid #2a2a2a;border-bottom:5px solid #2a2a2a}
.stat{width:200px;text-align:center;color:#fff;top:30px}
.stat .n{font-size:30px;font-weight:600;margin-top:12px}
.stat .l{font-size:12px;font-weight:600;margin-top:14px}

/* testimonials */
.quote{width:417px;height:185px;background:#fff;box-shadow:0 1px 10px rgba(0,0,0,.08)}
.quote .q{position:absolute;left:18px;top:8px;font-size:80px;font-weight:700;color:var(--orange);opacity:.35;line-height:80px}
.quote p{position:absolute;left:32px;top:52px;width:355px;font-size:13px;line-height:22.5px;font-style:italic;color:#888;font-weight:300}
.quote .who{position:absolute;right:86px;top:191px;font-size:12.5px;font-weight:600;color:var(--orange)}
.quote .who b{color:#333;font-size:10px;margin-left:8px}
.avatar{position:absolute;width:50px;height:50px;border-radius:50%;background:#bdbdbd;border:3px solid #fff;box-shadow:0 1px 5px rgba(0,0,0,.2)}
.dot{width:12px;height:12px;border-radius:50%;border:2px solid #222}

/* why */
.why-photo{left:144px;top:2622px;width:491px;height:426px;background:linear-gradient(160deg,#f8cf7e,#d88a2e 45%,#5b3a1e 100%)}
.why-card{left:582px;top:2637px;width:474px;height:396px;background:#fff;box-shadow:0 2px 14px rgba(0,0,0,.1);padding:42px 46px}
.why-card p{font-size:11.5px;line-height:19.5px;color:var(--text);font-weight:300;margin-top:18px}

/* contact */
.contact-title{left:245px;top:3145px}
.contact-info{left:246px;top:3220px;color:var(--text)}
.big-phone{font-size:38px;font-weight:600;color:var(--orange);margin-top:18px}
.field{left:610px;width:343px;border:1px solid #ddd;font-size:11px;color:#888;padding:0 20px;display:flex;align-items:center;justify-content:space-between}
.submit{left:610px;top:3371px;width:343px;height:36px;font-size:12px}

/* subscribe */
.subscribe{left:236px;top:3462px;width:727px;height:78px;background:#fff;box-shadow:0 2px 12px rgba(0,0,0,.12);z-index:2}
.footer{left:0;top:3513px;width:1200px;height:333px;background:linear-gradient(180deg,#5d5a4f,#3c3a35 60%,#2b2a27)}
.fcol{top:79px;color:#fff;font-size:11px}
.fcol h4{font-size:15px;font-weight:600;margin-bottom:14px}
.fcol li{list-style:none;height:34px}
.copy{left:0;top:3846px;width:1200px;height:45px;background:var(--orange);color:#fff;font-size:10.5px;text-align:center;line-height:45px}
</style>
</head>
<body>

<div class="abs topbar">
  <div class="abs phone">&#9742; (888) 123-4567</div>
  <div class="abs social"><span></span><span></span><span></span><span></span></div>
</div>

<header class="abs header">
  <div class="abs logo"><div class="mark"></div>QUARRYBEND</div>
  <a class="abs btn btn-grad apply">Apply for a job</a>
  <nav class="abs nav"><a>Home</a><a>About Us</a><a>Divisions</a><a>Supplies</a><a>Gallery</a><a>Contact Us</a></nav>
  <svg class="abs search" width="14" height="14" viewBox="0 0 14 14"><circle cx="6" cy="6" r="4.5" fill="none" stroke="#222" stroke-width="2"/><path d="M9.5 9.5 13 13" stroke="#222" stroke-width="2"/></svg>
</header>

<section class="abs hero" role="img" aria-label="Construction crew silhouettes at sunset with a worker holding a blue hard hat">
  <div class="abs arrow-box" style="left:23px;top:267px"><svg width="10" height="12"><path d="M8 1 2 6l6 5" fill="none" stroke="#222" stroke-width="2.5"/></svg></div>
  <div class="abs arrow-box" style="left:1144px;top:267px"><svg width="10" height="12"><path d="M2 1l6 5-6 5" fill="none" stroke="#222" stroke-width="2.5"/></svg></div>
  <a class="abs btn btn-grad b1">Learn more</a>
  <a class="abs btn b2">Contact us</a>
</section>
<div class="abs hero-text" style="top:345px">
  <div class="w">Welcome To</div>
  <div class="h">QUARRYBEND <em>BUILDING</em><br>COMPANY</div>
</div>

<div class="abs about-photo" role="img" aria-label="Two businessmen reviewing building plans on site"></div>
<h2 class="abs about-title">About Us</h2>
<div class="abs rule" style="left:543px;top:878px"></div>
<div class="abs about-text">Lorem Ipsum proin gravida nibh vel velit auctor aliquet. Aenean sollicitudin, lorem quis bibendum auctor, nisi elit consequat ipsum, nec sagittis sem nibh id elit. Duis sed odio sit amet nibh vulputate cursus a sit amet mauris. Morbi accumsan ipsum velit. Nam nec tellus a odio tincidunt auctor a ornare odio. Sed non mauris vitae erat consequat.</div>
<a class="abs btn btn-grad" style="left:538px;top:1009px;width:124px;height:37px">Read more</a>
<div class="abs years">10</div>
<div class="abs years-label">Years in<br>Business</div>

<div class="abs division" style="left:30px;top:1198px"><h3>Industrial</h3><p>Duis sed odio sit amet nibh vulputate cursus a sit amet mauris. Morbi accumsan ipsum velit. Nam nec tellus.</p></div>
<div class="abs division" style="left:418px;top:1198px"><h3>Commercial</h3><p>Duis sed odio sit amet nibh vulputate cursus a sit amet mauris. Morbi accumsan ipsum velit. Nam nec tellus.</p></div>
<div class="abs division" style="left:806px;top:1198px"><h3>Residential</h3><p>Duis sed odio sit amet nibh vulputate cursus a sit amet mauris. Morbi accumsan ipsum velit. Nam nec tellus.</p></div>
<div class="abs div-icon" role="img" aria-label="Factory illustration" style="left:182px;top:1174px"></div>
<div class="abs div-icon" role="img" aria-label="Office block illustration" style="left:570px;top:1174px"></div>
<div class="abs div-icon" role="img" aria-label="House illustration" style="left:958px;top:1174px"></div>

<div class="abs services-bg" role="img" aria-label="Faint cranes and building skyline"></div>
<h2 class="abs center-title" style="top:1407px">Our Services</h2>
<div class="abs rule center-rule" style="top:1456px"></div>

<div class="abs service" style="left:168px;top:1488px"><div class="band"></div><div class="ph" role="img" aria-label="Excavator demolishing a building" style="background:linear-gradient(160deg,#9fb7cf,#7e6d5a 60%,#4b3c2e)"></div><h3>Demolition</h3><p>Duis sed odio sit amet nibhvul putate cursus a sit amet mauris. Morbi accums.</p><svg class="go" width="20" height="14"><path d="M1 7h16M11 1l6 6-6 6" fill="none" stroke="#f6ac25" stroke-width="2"/></svg></div>
<div class="abs service" style="left:461px;top:1488px"><div class="band"></div><div class="ph" role="img" aria-label="Surveying instrument on a tripod" style="background:linear-gradient(160deg,#d8c9b1,#8b6c4d 60%,#4a3624)"></div><h3>Grading</h3><p>Duis sed odio sit amet nibhvul putate cursus a sit amet mauris. Morbi accums.</p><svg class="go" width="20" height="14"><path d="M1 7h16M11 1l6 6-6 6" fill="none" stroke="#f6ac25" stroke-width="2"/></svg></div>
<div class="abs service" style="left:754px;top:1488px"><div class="band"></div><div class="ph" role="img" aria-label="Building frame with tower cranes" style="background:linear-gradient(160deg,#7fb2e0,#c7d3de 55%,#8a8f94)"></div><h3>Constructions</h3><p>Duis sed odio sit amet nibhvul putate cursus a sit amet mauris. Morbi accums.</p><svg class="go" width="20" height="14"><path d="M1 7h16M11 1l6 6-6 6" fill="none" stroke="#f6ac25" stroke-width="2"/></svg></div>

<div class="abs sm-arrow" style="left:569px;top:1889px"><svg width="8" height="10"><path d="M6 1 2 5l4 4" fill="none" stroke="#222" stroke-width="2"/></svg></div>
<div class="abs sm-arrow" style="left:606px;top:1889px"><svg width="8" height="10"><path d="M2 1l4 4-4 4" fill="none" stroke="#222" stroke-width="2"/></svg></div>

<section class="abs stats" role="img" aria-label="Construction machinery behind an orange overlay">
  <div class="abs stat" style="left:189px"><svg width="26" height="30" viewBox="0 0 26 30"><circle cx="13" cy="9" r="7" fill="#fff"/><path d="M1 30c0-9 5-12 12-12s12 3 12 12z" fill="#fff"/></svg><div class="n">1780</div><div class="l">CLIENT</div></div>
  <div class="abs stat" style="left:396px"><svg width="30" height="30" viewBox="0 0 30 30"><rect x="1" y="12" width="6" height="17" fill="#fff"/><path d="M9 13l7-11c3 0 4 2 3 5l-2 5h10c2 0 3 2 2 4l-3 11c-1 2-2 2-3 2H9z" fill="#fff"/></svg><div class="n">1560</div><div class="l">SATISFIED</div></div>
  <div class="abs stat" style="left:603px"><svg width="32" height="28" viewBox="0 0 32 28"><path d="M11 5V2h10v3" fill="none" stroke="#fff" stroke-width="3"/><rect x="1" y="6" width="30" height="21" rx="2" fill="#fff"/><rect x="13" y="13" width="6" height="4" fill="#f29f1a"/></svg><div class="n">1640</div><div class="l">PROJECTS DONE</div></div>
  <div class="abs stat" style="left:810px"><svg width="32" height="30" viewBox="0 0 32 30"><path d="M8 2h16v9a8 8 0 0 1-16 0z" fill="#fff"/><path d="M8 5H2c0 6 3 9 7 9M24 5h6c0 6-3 9-7 9" fill="none" stroke="#fff" stroke-width="2.5"/><rect x="14" y="18" width="4" height="6" fill="#fff"/><rect x="9" y="24" width="14" height="4" fill="#fff"/></svg><div class="n">1402</div><div class="l">AWARDS</div></div>
</section>

<h2 class="abs center-title" style="top:2205px">Client Says About Us</h2>
<div class="abs rule center-rule" style="top:2254px"></div>

<div class="abs quote" style="left:-285px;top:2298px"><p>Lorem ipsum dolor sit amet, consectetur adipiscing elit, sed do eiusmod tempor incididunt ut labore et dolore magna aliqua. Ut enim ad minim veniam, quis nostrud exercitation ullamco laboris nisi ut aliquip ex ea commodo consequat.</p><div class="who">Jane Doe<b>CEO</b></div><div class="avatar" role="img" aria-label="Client portrait" style="left:302px;top:172px"></div></div>
<div class="abs quote" style="left:172px;top:2298px"><div class="q">&ldquo;</div><p>Lorem ipsum dolor sit amet, consectetur adipiscing elit, sed do eiusmod tempor incididunt ut labore et dolore magna aliqua. Ut enim ad minim veniam, quis nostrud exercitation ullamco laboris nisi ut aliquip ex ea commodo consequat.</p><div class="who">Carl John<b>CEO</b></div><div class="avatar" role="img" aria-label="Client portrait" style="left:347px;top:158px"></div></div>
<div class="abs quote" style="left:610px;top:2298px"><div class="q">&ldquo;</div><p>Lorem ipsum dolor sit amet, consectetur adipiscing elit, sed do eiusmod tempor incididunt ut labore et dolore magna aliqua. Ut enim ad minim veniam, quis nostrud exercitation ullamco laboris nisi ut aliquip ex ea commodo consequat.</p><div class="who">John Doe<b>CEO</b></div><div class="avatar" role="img" aria-label="Client portrait" style="left:347px;top:158px"></div></div>
<div class="abs quote" style="left:1047px;top:2298px"><div class="q">&ldquo;</div><p>Lorem ipsum dolor sit amet, consectetur adipiscing elit, sed do eiusmod tempor incididunt ut labore et dolore magna aliqua. Ut enim ad minim veniam, quis nostrud exercitation ullamco laboris nisi ut aliquip ex ea commodo consequat.</p></div>

<div class="abs dot" style="left:575px;top:2555px"></div>
<div class="abs dot" style="left:594px;top:2555px;border-color:var(--orange)"></div>
<div class="abs dot" style="left:613px;top:2555px"></div>

<div class="abs why-photo" role="img" aria-label="Excavator digging earth at sunset"></div>
<div class="abs why-card">
  <h2>Why Choose Us?</h2>
  <div class="rule" style="margin-top:18px"></div>
  <p>Lorem ipsum dolor sit amet, consectetur adipisicing elit, sed do eiusmod tempor incididunt ut labore et dolore magna aliqua. Ut enim ad minim veniam, quis nostrud exercitation ullamco laboris nisi ut aliquip ex ea commodo consequat. Duis aute irure dolor in reprehenderit in voluptate velit esse cillum dolore eu fugiat nulla pariatur. Excepteur sint occaecat.</p>
  <p>cupidatat non proident, sunt in culpa qui officia deserunt mollit anim id est laborum. Sed ut perspiciatis unde omnis iste natus error sit voluptatem accusantium.</p>
  <a class="btn btn-grad" style="width:124px;height:35px;margin-top:22px">Read more</a>
</div>

<h2 class="abs contact-title">Contact Us</h2>
<div class="abs rule" style="left:246px;top:3193px"></div>
<div class="abs contact-info">
  <div style="font-size:13px">NEED HELP? CALL US</div>
  <div class="big-phone">+(888) 23-4567</div>
  <div style="font-size:13px;margin-top:16px">Abc Ave 123 Street Example City KSA.</div>
  <div style="font-size:13px;margin-top:26px;color:var(--orange);font-weight:500">info@example.com</div>
</div>
<div class="abs field" style="top:3138px;height:35px">Name:<svg width="14" height="14"><circle cx="7" cy="4" r="3.5" fill="#f6ac25"/><path d="M0 14c0-5 3-6 7-6s7 1 7 6z" fill="#f6ac25"/></svg></div>
<div class="abs field" style="top:3190px;height:33px">Email:<svg width="15" height="11"><rect width="15" height="11" rx="1" fill="#f6ac25"/><path d="M1 1l6.5 5L14 1" fill="none" stroke="#fff" stroke-width="1.3"/></svg></div>
<div class="abs field" style="top:3240px;height:111px;align-items:flex-start;padding-top:14px">Message:<svg width="16" height="13"><ellipse cx="7" cy="5" rx="7" ry="5" fill="#f6ac25"/><path d="M2 8l-1 4 4-2" fill="#f6ac25"/></svg></div>
<a class="abs btn btn-grad submit">Submit</a>

<div class="abs footer" role="img" aria-label="Worker in a high-visibility vest, dimmed">
  <div class="abs" style="left:227px;top:140px;width:100px;text-align:center;color:var(--orange);font-size:14px;font-weight:600"><div style="width:20px;height:20px;background:var(--orange);margin:0 auto 8px"></div>QUARRYBEND</div>
  <ul class="abs fcol" style="left:391px"><h4>SITE MAP</h4><li>&rsaquo; Home</li><li>&rsaquo; About Us</li><li>&rsaquo; Divisions</li><li>&rsaquo; Supplies</li><li>&rsaquo; Gallery</li><li>&rsaquo; Apply For A Job</li></ul>
  <ul class="abs fcol" style="left:610px"><h4>USEFUL LINKS</h4><li>&rsaquo; Terms &amp; Conditions</li><li>&rsaquo; Blogs</li><li>&rsaquo; Privacy Policy</li><li>&rsaquo; Testimonials</li><li>&rsaquo; Partners</li></ul>
  <ul class="abs fcol" style="left:831px"><h4>CONTACT US</h4><li>&#9679; 1234 Street Name, City,</li><li style="padding-left:20px">Example Country.</li><li>&#9742; (123) 456-7890</li><li>&#9993; info@example.com</li><li><div class="social"><span style="width:18px;height:18px;background:#fff"></span><span style="width:18px;height:18px;background:#fff"></span><span style="width:18px;height:18px;background:#fff"></span><span style="width:18px;height:18px;background:#fff"></span></div></li></ul>
</div>

<div class="abs subscribe">
  <div class="abs" style="left:75px;top:22px;font-size:20px;font-weight:700;color:var(--orange);line-height:20px">SUBSCRIBE</div>
  <div class="abs" style="left:75px;top:44px;font-size:11.5px;font-weight:600">OUR NEWSLETTER</div>
  <div class="abs" style="left:312px;top:26px;width:236px;height:28px;border:1px solid #ddd;border-radius:3px;font-size:10px;font-style:italic;color:#aaa;padding:8px 16px">Your Email Address*</div>
  <a class="abs btn btn-grad" style="left:574px;top:26px;width:84px;height:28px;font-size:11px">Send</a>
</div>

<div class="abs copy">Copyright &copy; <b>Quarrybend Building Company</b> 2019 | All Rights Reserved.</div>

</body>
</html>
```